Web Design for Financial Consulting Company

We need a website design for a financial consulting company "Kelvane Consulting". We build financial models, scenario analysis, handle the budgeting process and provide temporary staffing. I have over 10 years of experience. My Excel expertise and analytical savvy has saved clients over $17 million in profit.

Target Market(s)

Small to medium businesses

Industry/Entity Type

Financial Consulting

Number of Pages Required

4 page

Requirements
Must have
• Professional looking
Nice to have
• A little futuristic looking

```html
<!DOCTYPE html>
<html lang="en">
<head>
<meta charset="utf-8">
<title>Kelvane Consulting</title>
<link href="https://fonts.googleapis.com/css2?family=Outfit:wght@300;400;500;600;700;800&display=swap" rel="stylesheet">
<style>
:root{
  --blue:#0aa1ee;
  --ink:#111319;
  --dark:#13151d;
  --text:#2a2d36;
  --muted:#5a5f6b;
  --card:#eef2f9;
  --line:#c9ccd3;
  --ghost:#e7eaf0;
  --white:#ffffff;
}
*{margin:0;padding:0;box-sizing:border-box}
html,body{width:1200px;height:3797px;overflow:hidden}
body{position:relative;background:var(--white);font-family:"Outfit",sans-serif;color:var(--text)}
.abs{position:absolute}
.hero-bg{left:0;top:0;width:1200px;height:675px;background:radial-gradient(ellipse at 65% 40%,#2a2e38 0%,#171920 55%,#0f1116 100%)}
.header-rule{left:0;top:118px;width:1200px;height:1px;background:rgba(255,255,255,.08)}
.brand{display:flex;align-items:center;gap:10px;font-weight:600;font-size:22px;letter-spacing:1.5px;color:var(--white)}
.brand-mark{width:26px;height:26px;border:2.5px solid var(--white)}
.brand small{font-size:22px}
.nav{left:619px;top:50px;display:flex;gap:26px;font-size:15px;color:var(--white)}
.nav .active{position:relative}
.nav .active::after{content:"";position:absolute;left:0;bottom:-8px;width:12px;height:2px;background:var(--blue)}
.btn{display:flex;align-items:center;justify-content:space-between;background:var(--white);color:var(--ink);font-size:14px;border:2px solid var(--white)}
.btn span{padding-left:28px}
.btn i{font-style:normal;width:40px;height:100%;background:var(--blue);color:var(--white);display:flex;align-items:center;justify-content:center;font-size:24px;font-weight:300}
.btn.light{background:var(--card);border-color:var(--card)}
.hero-kicker{left:161px;top:216px;font-size:17px;color:var(--white)}
.hero-title{left:158px;top:246px;font-size:54px;font-weight:500;line-height:60px;color:var(--white)}
.hero-title em{font-style:normal;color:var(--blue)}
.dots{left:161px;top:610px;display:flex;gap:15px}
.dots b{width:6px;height:6px;background:var(--white)}
.dots b.on{background:var(--blue)}
.photo{background:linear-gradient(160deg,#b9c0c8 0%,#6d737c 45%,#3a3430 100%)}
.ghost{font-size:170px;font-weight:700;line-height:1;color:transparent;-webkit-text-stroke:1.5px var(--ghost);white-space:nowrap;letter-spacing:4px}
.stat{left:0;top:856px;width:1200px;text-align:center;font-size:28px;line-height:31px;color:var(--ink)}
.stat mark{background:var(--blue);color:var(--white);padding:0 8px}
.stat strong{font-style:italic}
.kicker{font-size:17px;color:var(--ink)}
.kicker em{font-style:normal;color:var(--blue)}
.title{font-size:45px;font-weight:700;color:var(--ink);letter-spacing:.5px}
.blue-block{background:var(--blue)}
.about-copy{left:650px;top:1136px;width:360px;font-size:18px;line-height:27px;color:var(--text)}
.card{background:var(--card);width:283px;height:376px;text-align:center;padding-top:58px}
.card svg{width:60px;height:62px}
.card h3{margin-top:30px;font-size:17px;font-weight:700;color:var(--ink);line-height:22px;text-transform:uppercase}
.card p{margin:8px auto 0;width:210px;font-size:14px;line-height:22px;color:var(--text)}
.card a{position:absolute;left:0;right:0;bottom:44px;font-size:14px;font-weight:600;color:var(--ink);text-decoration:underline}
.card.on{border-bottom:7px solid var(--blue)}
.field{left:161px;width:371px;border-bottom:1px solid var(--line);font-size:13px;color:var(--ink);padding:0 0 10px 22px}
.news{left:159px;top:3290px;width:877px;height:143px;background:var(--blue);color:var(--white)}
.news h4{position:absolute;left:70px;top:48px;font-size:22px;font-weight:400;line-height:22px}
.news h4 b{display:block;font-size:33px;font-weight:700;line-height:36px}
.news .mail{position:absolute;left:507px;top:62px;width:300px;border-bottom:1px solid rgba(255,255,255,.7);padding:0 0 12px 22px;font-size:13px}
.footer-bg{left:0;top:3364px;width:1200px;height:433px;background:linear-gradient(180deg,#1a1c23 0%,#101218 100%)}
.foot-about{left:161px;top:3567px;width:300px;font-size:11px;line-height:18px;color:#d7d9de}
.foot-h{font-size:14px;font-weight:600;color:var(--white);letter-spacing:.3px}
.foot-list{left:582px;top:3540px;list-style:none;font-size:13px;line-height:23.5px;color:#d7d9de}
.foot-list .cur{color:var(--white);font-weight:600}
.social{left:822px;top:3570px;display:flex;gap:9px}
.social b{width:18px;height:18px;border-radius:50%;background:var(--blue)}
.social b:nth-child(3){background:#e5383b}
.social b:nth-child(4){background:#1d5fa8}
.foot-rule{left:161px;top:3732px;width:877px;height:1px;background:rgba(255,255,255,.12)}
.copy{top:3752px;font-size:13px;color:#d7d9de}
.copy em{font-style:normal;color:var(--blue);font-weight:600}
</style>
</head>
<body>

<div class="abs hero-bg" role="img" aria-label="Dark blurred office meeting backdrop"></div>
<div class="abs header-rule"></div>

<div class="abs brand" style="left:161px;top:42px"><span class="brand-mark"></span><span>KELVANE</span></div>
<nav class="abs nav"><span class="active">Home</span><span>About Us</span><span>Services</span></nav>
<div class="abs btn" style="left:862px;top:35px;width:176px;height:48px"><span>Contact Us</span><i>+</i></div>

<div class="abs hero-kicker">KELVANE CONSULTING</div>
<h1 class="abs hero-title">Helping Your<br><em>Finance Team</em> &amp;<br><em>Increasing Profit</em></h1>
<div class="abs btn" style="left:161px;top:455px;width:177px;height:48px"><span>Let's Explore</span><i>+</i></div>
<div class="abs dots"><b></b><b class="on"></b><b></b></div>

<div class="abs photo" style="left:607px;top:167px;width:431px;height:576px" role="img" aria-label="Photo of a consultant in a grey suit reviewing documents with a colleague"></div>

<div class="abs ghost" style="left:-4px;top:656px">EXPERTISE</div>

<p class="abs stat">With over <mark>10 Years Of Experience,</mark><br>I have successfully <mark>Increased</mark> profitability for clients by <strong>$17M.</strong></p>

<div class="abs blue-block" style="left:0;top:1101px;width:161px;height:234px"></div>
<div class="abs photo" style="left:161px;top:1002px;width:432px;height:448px;background:linear-gradient(150deg,#d9dde2 0%,#8d939b 50%,#2c3340 100%)" role="img" aria-label="Photo of two businessmen discussing work at a laptop"></div>
<div class="abs ghost" style="left:890px;top:990px;font-size:140px">ABOUT</div>
<div class="abs kicker" style="left:650px;top:1040px">KELVANE <em>CONSULTING</em></div>
<h2 class="abs title" style="left:650px;top:1060px">ABOUT US</h2>
<p class="abs about-copy">I am an experienced Finance professional who develops strategic financial plans, provides insightful analysis, and supports decision-making. With over 10 years of experience, I have successfully increased profitability for clients by $17M.</p>
<div class="abs btn light" style="left:650px;top:1325px;width:173px;height:46px"><span>Read More</span><i>+</i></div>

<div class="abs ghost" style="left:-70px;top:1522px;font-size:140px">WHAT WE PROVIDE</div>
<div class="abs kicker" style="left:0;width:1200px;text-align:center;top:1558px">KELVANE <em>CONSULTING</em></div>
<h2 class="abs title" style="left:0;width:1200px;text-align:center;top:1577px">OUR SERVICES</h2>

<div class="abs card" style="left:161px;top:1708px">
  <svg viewBox="0 0 60 62" fill="none" stroke="#111319" stroke-width="2"><rect x="8" y="10" width="34" height="44"/><path d="M14 4h34v44"/><path d="M14 22h10M14 30h16M14 38h16M14 46h12"/><circle cx="46" cy="38" r="9"/><path d="M46 33v10M43 36h5M44 40h4"/></svg>
  <h3>Financial Models<br>– Projects</h3>
  <p>Financial analysis, scenario modeling, pricing analysis, projects</p>
  <a>Read More</a>
</div>
<div class="abs card on" style="left:460px;top:1708px">
  <svg viewBox="0 0 60 62" fill="none" stroke="#111319" stroke-width="2"><rect x="18" y="4" width="30" height="38"/><path d="M24 12h18M24 20h18M24 28h12"/><rect x="4" y="30" width="26" height="28"/><path d="M9 36h16M9 44h4M15 44h4M21 44h4M9 51h4M15 51h4M21 51h4"/><circle cx="46" cy="46" r="9"/><path d="M46 41v10"/><path d="M50 8l8-4-2 10"/></svg>
  <h3>Budgeting Process</h3>
  <p>Building budgets from scratch, revamping current process to be more robust and scalable.</p>
  <a>Read More</a>
</div>
<div class="abs card" style="left:756px;top:1708px">
  <svg viewBox="0 0 60 62" fill="none" stroke="#111319" stroke-width="2"><rect x="20" y="4" width="20" height="16"/><circle cx="30" cy="10" r="3"/><circle cx="30" cy="34" r="6"/><circle cx="12" cy="30" r="5"/><circle cx="48" cy="30" r="5"/><path d="M4 56c0-10 4-16 8-16s8 6 8 16M40 56c0-10 4-16 8-16s8 6 8 16M20 58c0-10 4-16 10-16s10 6 10 16"/></svg>
  <h3>Temporary Staffing</h3>
  <p>Years of Financial Planning and Analysis experience across multiple industries can help temporary staffing needs.</p>
  <a>Read More</a>
</div>
<div class="abs card" style="left:317px;top:2102px">
  <svg viewBox="0 0 60 62" fill="none" stroke="#111319" stroke-width="2"><rect x="8" y="4" width="34" height="46"/><rect x="14" y="10" width="34" height="46"/><path d="M20 20h22M20 28h22M20 36h14"/><path d="M34 56l6-10h14l-4 10z"/><path d="M24 48v6M21 51h6"/></svg>
  <h3>Data Cleansing</h3>
  <p>Financial analysis, scenario modeling, pricing analysis, projects</p>
  <a>Read More</a>
</div>
<div class="abs card" style="left:615px;top:2102px">
  <svg viewBox="0 0 60 62" fill="none" stroke="#111319" stroke-width="2"><circle cx="28" cy="9" r="5"/><rect x="6" y="18" width="24" height="32"/><path d="M11 26h14M11 34h14M11 42h10"/><rect x="34" y="22" width="20" height="34"/><path d="M38 30h12M38 38h12M38 46h12"/><circle cx="30" cy="46" r="6"/></svg>
  <h3>Process Improvement</h3>
  <p>Month end close, reporting, budgeting</p>
  <a>Read More</a>
</div>

<div class="abs ghost" style="left:-10px;top:2600px;font-size:140px">CONTACT</div>
<div class="abs kicker" style="left:161px;top:2639px">KELVANE <em>CONSULTING</em></div>
<h2 class="abs title" style="left:161px;top:2658px">LET'S CONNECT</h2>
<div class="abs field" style="top:2767px">First Name</div>
<div class="abs field" style="top:2819px">Last Name</div>
<div class="abs field" style="top:2872px">Phone</div>
<div class="abs field" style="top:2924px">Email</div>
<div class="abs field" style="top:3023px">Message</div>
<div class="abs btn light" style="left:161px;top:3081px;width:173px;height:44px"><span>Let's Explore</span><i>+</i></div>

<div class="abs blue-block" style="left:1052px;top:2730px;width:148px;height:309px"></div>
<div class="abs photo" style="left:620px;top:2603px;width:432px;height:563px;background:linear-gradient(170deg,#dfe5ea 0%,#b7c3cf 45%,#6d7f93 100%)" role="img" aria-label="Photo of a smiling businessman at his desk reaching out for a handshake"></div>

<div class="abs footer-bg" role="img" aria-label="Dark office backdrop"></div>
<div class="abs news">
  <h4>Subscribe Our<b>Newsletter</b></h4>
  <div class="mail">Enter Email Address.</div>
  <svg class="abs" style="left:765px;top:63px" width="16" height="16" viewBox="0 0 16 16" fill="#fff"><path d="M15 1L1 7l5 2 2 6z"/></svg>
</div>

<div class="abs brand" style="left:161px;top:3513px"><span class="brand-mark"></span><span>KELVANE</span></div>
<p class="abs foot-about">I am an experienced Finance professional who develops strategic financial plans, provides insightful analysis, and supports decision-making. With over 10 years of experience, I have successfully increased profitability for clients by $17M.</p>

<div class="abs foot-h" style="left:582px;top:3507px">QUICK LINKS</div>
<ul class="abs foot-list"><li>Home</li><li class="cur">About Us</li><li>Services</li><li>Contact Us</li></ul>

<div class="abs foot-h" style="left:822px;top:3507px">FOLLOW US</div>
<div class="abs" style="left:822px;top:3536px;font-size:13px;color:#d7d9de">Get Latest Updates!</div>
<div class="abs social"><b></b><b></b><b></b><b></b></div>
<div class="abs btn" style="left:822px;top:3611px;width:176px;height:47px"><span style="padding-left:38px">Connect</span><i>+</i></div>

<div class="abs foot-rule"></div>
<div class="abs copy" style="left:161px">Copyright @ 2023. <em>KELVANE</em>. All Right Reserved.</div>
<div class="abs copy" style="left:826px">Terms &amp; Conditions | Privacy Policy</div>

</body>
</html>
```